Rising Paths Web Design

I am starting a new company that will provide LIFE COACHING services - I have tried to design a website, but it's too complicated. Right now, it's just me - I'm the only person that will provide services through the website - I have used artmarket to purchase a logo (see below). I want to be able to update the website myself, but need a template - basic design. Because I am not technologically savvy enough to explain in words - I basically want to have a website that will provide basic information about my services (coaching), a page about me and my background, hopefully scheduling possibilities, and testimonials — also a page for writing/blogs. I bought a website through NetHarbor - so when I have a template, I guess I”d use that - but maybe I’ll need to work with a designer to actually get it up on the internet. I have a head shot that I’ll upload, too.
Target Market(s)
Clients from the independent (private school) world - teachers, administrators
Number of Pages Required
4 page
Look and feel
Each slider illustrates characteristics of the customer's brand and the style your logo design should communicate.

```html
<!DOCTYPE html>
<html lang="en">
<head>
<meta charset="utf-8">
<title>Rising Paths Coaching</title>
<link href="https://fonts.googleapis.com/css2?family=Playfair+Display:wght@400;700&family=Open+Sans:wght@400;600;700&family=Arimo:wght@400;700&display=swap" rel="stylesheet">
<style>
:root{
  --teal:#1bb3a1;
  --teal-dark:#0f8f80;
  --teal-light:#8fdcd2;
  --mint:#eef8f6;
  --ink:#111;
  --text:#555;
  --muted:#888;
  --white:#fff;
  --hero-dark:#1c2226;
  --hero-mid:#3a454b;
}
*{box-sizing:border-box;margin:0;padding:0}
html,body{width:1200px;height:5296px;overflow:hidden}
body{position:relative;background:var(--white);font-family:"Open Sans",Arial,sans-serif;color:var(--text)}
.abs{position:absolute}

/* header */
.topbar{left:0;top:0;width:1200px;height:45px;background:var(--teal)}
.navbar{left:0;top:45px;width:1200px;height:99px;background:#000}
.contact-strip{top:12px;left:315px;display:flex;gap:26px;color:#fff;font-family:"Playfair Display",Georgia,serif;font-size:15px;align-items:center}
.contact-strip span{display:flex;align-items:center;gap:8px}
.socials{display:flex;gap:18px}
.socials i{display:block;width:14px;height:14px;border-radius:50%;background:currentColor}
.top-socials{top:15px;right:70px;color:#fff}
.logo{left:40px;top:10px;width:122px;height:122px;border-radius:50%;background:#fff;border:3px solid var(--teal-light);display:flex;align-items:center;justify-content:center;text-align:center;color:var(--teal-dark);font-family:"Playfair Display",Georgia,serif;font-size:15px;line-height:1.15}
.nav{top:70px;left:280px;display:flex;gap:34px;font-family:"Playfair Display",Georgia,serif;font-weight:700;font-size:17px;color:#fff}
.nav .active{color:var(--teal)}
.book-btn{left:953px;top:60px;width:227px;height:55px;border-radius:28px;background:var(--teal);color:#fff;font-family:"Playfair Display",Georgia,serif;font-weight:700;font-size:14px;line-height:15px;text-align:center;padding-top:12px}
.book-btn b{position:absolute;right:34px;top:16px;font-size:18px}

/* hero */
.hero-img{left:0;top:144px;width:1200px;height:656px;background:linear-gradient(90deg,var(--hero-dark) 0%,var(--hero-mid) 55%,var(--hero-dark) 100%)}
.hero-title{left:121px;top:328px;width:600px;font-family:"Playfair Display",Georgia,serif;font-weight:700;font-size:47px;line-height:52px;color:var(--teal)}
.hero-sub{left:121px;top:514px;font-size:12px;color:var(--teal)}
.hero-btn{left:121px;top:556px;width:170px;height:38px;border:2px solid var(--teal);border-radius:20px;color:#fff;font-size:12px;font-weight:600;text-align:center;line-height:34px}
.hero-arrow{top:430px;color:var(--teal);font-size:48px;line-height:1}
.hero-wave{left:0;top:590px}
.dots{display:flex;gap:8px}
.dots i{display:block;width:10px;height:10px;border-radius:50%;background:#999}
.dots i.on{background:var(--teal)}

/* about */
.h2{font-family:"Playfair Display",Georgia,serif;font-size:32px;color:var(--ink);text-align:center}
.about-text{left:150px;top:895px;width:442px;font-size:11.5px;line-height:21px;color:#333;text-align:justify}
.about-text p+p{margin-top:18px}
.skill{left:150px;width:442px}
.skill label{display:block;font-size:11px;letter-spacing:2px;color:#333;margin-bottom:6px}
.track{height:8px;background:#ddd;position:relative}
.fill{height:8px;background:var(--teal);position:relative}
.fill em{position:absolute;right:6px;top:-1px;font-style:normal;font-size:7px;color:#cfeee9}
.portrait-ring{left:645px;top:857px;width:320px;height:320px;border-radius:50%;border:2px solid var(--teal)}
.portrait{left:657px;top:869px;width:296px;height:296px;border-radius:50%;background:linear-gradient(180deg,#c9c3b4 0%,#d8b896 100%)}
.about-social{left:763px;top:1196px;color:var(--teal)}
.contact-btn{left:750px;top:1247px;width:156px;height:41px;border-radius:21px;background:var(--teal);color:#fff;font-family:"Playfair Display",Georgia,serif;font-weight:700;font-size:16px;text-align:center;line-height:41px}
.cert-title{left:168px;top:1353px;font-family:"Playfair Display",Georgia,serif;font-size:33px;color:var(--ink)}
.explore{left:158px;top:1422px;font-size:11px;font-weight:700;color:var(--teal)}
.badge{top:1352px;height:93px;border-radius:10px;background:#1f4d6b}
.badge.round{border-radius:50%;background:#fff;border:8px solid var(--teal)}

/* benefits */
.benefit-bg{left:0;top:1500px;width:1200px;height:555px;background:linear-gradient(180deg,#fff 0%,var(--mint) 18%,var(--mint) 82%,#fff 100%)}
.benefit{width:300px;text-align:center}
.benefit .ico{width:86px;height:86px;margin:0 auto;border-radius:50%;border:3px solid var(--teal);display:flex;align-items:center;justify-content:center}
.benefit .ico span{width:58px;height:58px;border-radius:50%;background:var(--teal);display:flex;align-items:center;justify-content:center}
.benefit h3{font-family:"Playfair Display",Georgia,serif;font-size:22px;font-weight:700;color:var(--ink);margin-top:28px}
.benefit p{font-size:11px;line-height:22px;color:#666;margin:14px auto 0;width:280px}

/* services */
.sub{font-size:15px;color:var(--teal);text-align:center;line-height:23px;width:1200px;left:0}
.svc{width:276px;text-align:center}
.svc .img{height:185px;border-radius:0 0 26px 0;border-right:4px solid var(--teal-light);border-bottom:4px solid var(--teal-light)}
.svc h4{font-family:"Arimo",Arial,sans-serif;font-size:17px;font-weight:700;color:#222;margin-top:22px}
.svc p{font-size:11px;line-height:21px;color:#777;text-align:justify;padding:0 22px;margin-top:10px}
.svc a{display:block;font-size:10px;font-weight:700;color:var(--teal);margin-top:18px;text-decoration:none}

/* testimonials */
.testi-bg{left:0;top:3124px;width:1200px;height:640px;background:linear-gradient(180deg,#fff 0%,var(--mint) 20%,var(--mint) 80%,#fff 100%)}
.testi{width:268px;height:308px;background:#fff}
.testi .photo{position:absolute;left:44px;top:38px;width:100px;height:100px;border-radius:50%}
.testi .who{position:absolute;left:150px;top:60px;width:100px;text-align:center}
.testi .who b{display:block;font-family:"Playfair Display",Georgia,serif;font-weight:400;font-size:16px;color:#333;line-height:18px}
.testi .who small{display:block;font-size:9px;letter-spacing:2px;color:#999;margin-top:6px}
.testi .quote{position:absolute;left:23px;top:164px;width:224px;height:113px;background:var(--teal);color:#fff;font-size:10.5px;line-height:21px;text-align:center;padding:14px 12px}
.t-arrow{top:3530px;font-size:22px;color:#333}

/* blogs */
.blog{width:245px;background:#fff;box-shadow:0 2px 10px rgba(0,0,0,.06);text-align:center;padding-bottom:28px}
.blog .img{height:243px;border-radius:0 0 22px 0;border-right:4px solid var(--teal-light);border-bottom:4px solid var(--teal-light)}
.blog h4{font-family:"Arimo",Arial,sans-serif;font-size:16px;font-weight:700;color:#222;line-height:22px;margin-top:20px;padding:0 16px}
.blog p{font-size:11px;line-height:21px;color:#777;text-align:justify;padding:0 18px;margin-top:14px}
.blog a{display:block;font-size:10px;font-weight:700;color:var(--teal);margin-top:20px;text-decoration:none}

/* footer */
.footer-bg{left:0;top:4818px;width:1200px;height:412px;background:var(--mint)}
.foot-logo{left:150px;top:4850px;width:164px;height:136px;display:flex;align-items:center;justify-content:center;text-align:center;font-family:"Playfair Display",Georgia,serif;font-size:17px;color:var(--teal-dark)}
.foot-about{left:150px;top:4998px;width:218px;font-size:10.5px;line-height:20.5px;color:#666;text-align:justify}
.foot-h{top:4838px;font-family:"Playfair Display",Georgia,serif;font-weight:700;font-size:15px;color:#222}
.foot-links{left:438px;top:4918px;font-family:"Playfair Display",Georgia,serif;font-size:15px;line-height:37px;color:#444;list-style:none}
.foot-links li:first-child{color:var(--teal)}
.foot-contact{left:606px;font-family:"Playfair Display",Georgia,serif;font-size:14px;color:#333;display:flex;gap:18px;line-height:26px}
.foot-contact svg{flex:none;margin-top:5px}
.form-label{font-size:10px;color:#333}
.field{height:37px;background:#fff;border:1px solid #bbb;font-size:10px;color:#999;padding:11px 10px}
.schedule{left:836px;top:5113px;width:214px;height:37px;border-radius:19px;background:var(--teal);color:#fff;font-family:"Playfair Display",Georgia,serif;font-weight:700;font-size:14px;text-align:center;line-height:37px}
.copy{left:0;top:5230px;width:1200px;height:66px;background:#000;color:#fff;font-family:"Playfair Display",Georgia,serif;font-size:14px;text-align:center;line-height:66px}
</style>
</head>
<body>

<!-- header -->
<div class="abs topbar"></div>
<div class="abs navbar"></div>
<div class="abs contact-strip">
  <span><svg width="12" height="16" viewBox="0 0 12 16"><path d="M6 0a6 6 0 0 0-6 6c0 4.5 6 10 6 10s6-5.5 6-10a6 6 0 0 0-6-6zm0 8.5A2.5 2.5 0 1 1 6 3.5a2.5 2.5 0 0 1 0 5z" fill="#fff"/></svg>12/7 Maple Row Eastfield</span>
  <span><svg width="15" height="15" viewBox="0 0 24 24"><path d="M6.6 10.8a15 15 0 0 0 6.6 6.6l2.2-2.2a1 1 0 0 1 1-.25 11.4 11.4 0 0 0 3.6.57 1 1 0 0 1 1 1V20a1 1 0 0 1-1 1A17 17 0 0 1 3 4a1 1 0 0 1 1-1h3.5a1 1 0 0 1 1 1c0 1.25.2 2.45.57 3.57a1 1 0 0 1-.25 1z" fill="#fff"/></svg>+0198765432</span>
  <span><svg width="16" height="12" viewBox="0 0 16 12"><rect width="16" height="12" rx="1" fill="#fff"/><path d="M0 1l8 6 8-6" stroke="#1bb3a1" stroke-width="1.5" fill="none"/></svg>hello@mailbox.com</span>
</div>
<div class="abs socials top-socials"><i></i><i></i><i></i><i></i></div>
<div class="abs logo">Rising Paths</div>
<nav class="abs nav"><span class="active">Home</span><span>About Me</span><span>My Services</span><span>Testimonies</span><span>Blogs</span><span>Contact</span></nav>
<div class="abs book-btn">Book An<br>Appointment<b>›</b></div>

<!-- hero -->
<div class="abs hero-img" role="img" aria-label="Hero photo: a person facing a bright doorway in a dark wall"></div>
<div class="abs hero-title">Support Your Personal Development And Chase Your Dream</div>
<div class="abs hero-sub">Lorem ipsum dolor sit amet consectetur adipiscing elit dolor</div>
<div class="abs hero-btn">Get Started Today</div>
<div class="abs hero-arrow" style="left:18px">‹</div>
<div class="abs hero-arrow" style="right:18px">›</div>
<svg class="abs hero-wave" width="1200" height="215" viewBox="0 0 1200 215">
  <path d="M0 70 C180 170 420 170 640 120 C860 70 1050 50 1200 0 L1200 215 L0 215Z" fill="#7fd8cc"/>
  <path d="M0 95 C200 200 430 185 660 135 C880 88 1060 75 1200 30 L1200 215 L0 215Z" fill="#1bb3a1"/>
  <path d="M0 125 C220 215 450 195 680 150 C900 108 1070 100 1200 75 L1200 215 L0 215Z" fill="#fff"/>
</svg>
<div class="abs dots" style="left:582px;top:761px"><i></i><i class="on"></i></div>

<!-- about -->
<div class="abs h2" style="left:220px;top:838px;width:300px">About Me</div>
<div class="abs about-text">
  <p>Eu iusto dolorum pro, facer oportere duo ne. Cum ei commune instructior. Ne dicat qualisque ullamcorper ius, ubique dolorum consetetur in vis. Nisl commodo te sed.</p>
  <p>Diam donec adipiscing tristique risus nec. Vitae congue mauris rhoncus aenean vel. Feugiat nisl pretium fusce id velit ut tortor. Non diam phasellus vestibulum lorem. Etiam erat velit scelerisque in dictum. At auctor urna nunc id cursus. Odio ut sem nulla pharetra diam sit amet. Bibendum enim facilisis gravida neque convallis a cras semper. Eu feugiat pretium nibh ipsum consequat.</p>
</div>
<div class="abs skill" style="top:1122px"><label>Experience</label><div class="track"><div class="fill" style="width:80%"><em>80%</em></div></div></div>
<div class="abs skill" style="top:1170px"><label>Communication</label><div class="track"><div class="fill" style="width:94%"><em>94%</em></div></div></div>
<div class="abs skill" style="top:1217px"><label>Service</label><div class="track"><div class="fill" style="width:84%"><em>84%</em></div></div></div>
<div class="abs skill" style="top:1264px"><label>Success Rate</label><div class="track"><div class="fill" style="width:91%"><em>91%</em></div></div></div>
<div class="abs portrait-ring"></div>
<div class="abs portrait" role="img" aria-label="Head shot of the coach"></div>
<div class="abs socials about-social"><i></i><i></i><i></i><i></i></div>
<div class="abs contact-btn">Contact Me ›</div>

<div class="abs cert-title">I'm A Certified Coach</div>
<div class="abs explore">EXPLORE MORE »</div>
<div class="abs badge" style="left:555px;width:92px"></div>
<div class="abs badge round" style="left:740px;width:86px;height:86px;top:1356px"></div>
<div class="abs badge" style="left:920px;width:89px;border-radius:6px"></div>

<!-- benefits -->
<div class="abs benefit-bg"></div>
<div class="abs h2" style="left:0;top:1630px;width:1200px">Coaching Benefit</div>
<div class="abs benefit" style="left:150px;top:1695px">
  <div class="ico"><span><svg width="28" height="28" viewBox="0 0 24 24"><path d="M12 2c4 2 6 6 5 11l-3 3h-4l-3-3C6 8 8 4 12 2z" fill="#fff"/><circle cx="12" cy="9" r="2" fill="#1bb3a1"/><path d="M7 14l-3 4 4-1zM17 14l3 4-4-1zM10 17l2 5 2-5z" fill="#fff"/></svg></span></div>
  <h3>Achieve Life Goals</h3>
  <p>Lorem ipsum dolor sit amet, consectetur adipiscing elit. Ut elit tellus, luctus nec ullamcorper dapibus leo.</p>
</div>
<div class="abs benefit" style="left:450px;top:1695px">
  <div class="ico"><span><svg width="30" height="26" viewBox="0 0 30 26"><circle cx="11" cy="7" r="5" fill="#fff"/><path d="M1 24c0-6 4-10 10-10s10 4 10 10z" fill="#fff"/><circle cx="22" cy="9" r="3.5" fill="#fff"/><path d="M18 24c0-5 3-9 6-9s5 3 5 9z" fill="#fff"/></svg></span></div>
  <h3>Ask Consultancy</h3>
  <p>Lorem ipsum dolor sit amet, consectetur adipiscing elit. Ut elit tellus, luctus nec ullamcorper dapibus leo.</p>
</div>
<div class="abs benefit" style="left:750px;top:1695px">
  <div class="ico"><span><svg width="24" height="28" viewBox="0 0 24 28"><circle cx="12" cy="8" r="6" fill="#fff"/><path d="M1 27c0-7 5-11 11-11s11 4 11 11z" fill="#fff"/></svg></span></div>
  <h3>Self Development</h3>
  <p>Lorem ipsum dolor sit amet, consectetur adipiscing elit. Ut elit tellus, luctus nec ullamcorper dapibus leo.</p>
</div>

<!-- services -->
<div class="abs h2" style="left:0;top:2120px;width:1200px">My Services</div>
<div class="abs sub" style="top:2172px">Lorem ipsum dolor sit amet, consectetur adipiscing elit.<br>Mauris eros dolor pellentesque sed luctus dapibus lobortis orci.</div>

<div class="abs svc" style="left:158px;top:2267px"><div class="img" role="img" aria-label="Photo: person climbing steps at sunset" style="background:linear-gradient(180deg,#d98b3a,#7a4018)"></div><h4>Growth Career</h4><p>Lorem ipsum dolor sit amet, consectetur adipiscing elit. Morbi volutpat justo sed efficitur cursus. Mauris fringilla quam vitae lacinia.</p><a>LEARN MORE</a></div>
<div class="abs svc" style="left:462px;top:2267px"><div class="img" role="img" aria-label="Photo: person before a bright doorway" style="background:linear-gradient(180deg,#4a4240,#222)"></div><h4>Your Life Destination</h4><p>Lorem ipsum dolor sit amet, consectetur adipiscing elit. Morbi volutpat justo sed efficitur cursus. Mauris fringilla quam vitae lacinia.</p><a>LEARN MORE</a></div>
<div class="abs svc" style="left:766px;top:2267px"><div class="img" role="img" aria-label="Photo: couple under a night sky" style="background:linear-gradient(180deg,#2c4a78,#0d1a33)"></div><h4>Relationship Coaching</h4><p>Lorem ipsum dolor sit amet, consectetur adipiscing elit. Morbi volutpat justo sed efficitur cursus. Mauris fringilla quam vitae lacinia.</p><a>LEARN MORE</a></div>

<div class="abs svc" style="left:158px;top:2682px"><div class="img" role="img" aria-label="Photo: person jumping against a bright sky" style="background:linear-gradient(180deg,#8cc8e0,#d9b27a)"></div><h4>Long Career Advices</h4><p>Lorem ipsum dolor sit amet, consectetur adipiscing elit. Morbi volutpat justo sed efficitur cursus. Mauris fringilla quam vitae lacinia.</p><a>LEARN MORE</a></div>
<div class="abs svc" style="left:462px;top:2682px"><div class="img" role="img" aria-label="Photo: stressed man surrounded by clutter" style="background:linear-gradient(180deg,#8a8a8a,#2a2a2a)"></div><h4>Stress Management</h4><p>Lorem ipsum dolor sit amet, consectetur adipiscing elit. Morbi volutpat justo sed efficitur cursus. Mauris fringilla quam vitae lacinia.</p><a>LEARN MORE</a></div>
<div class="abs svc" style="left:766px;top:2682px"><div class="img" role="img" aria-label="Photo: business people in red and blue double exposure" style="background:linear-gradient(90deg,#e890a0,#6a86b4)"></div><h4>Self-Confidence Coaching</h4><p>Lorem ipsum dolor sit amet, consectetur adipiscing elit. Morbi volutpat justo sed efficitur cursus. Mauris fringilla quam vitae lacinia.</p><a>LEARN MORE</a></div>

<!-- testimonials -->
<div class="abs testi-bg"></div>
<div class="abs h2" style="left:0;top:3273px;width:1200px">Testimonials</div>
<div class="abs" style="left:0;top:3331px;width:1200px;text-align:center;font-size:11px;color:var(--teal)">Viverra lectus mauris ultrices eros in. Eget egestas purus viverra accumsan in nisl nulla nisi scelerisque eu vestibulum sed risus ultricies.</div>
<div class="abs t-arrow" style="left:153px">‹</div>
<div class="abs t-arrow" style="left:1036px">›</div>

<div class="abs testi" style="left:168px;top:3391px"><div class="photo" role="img" aria-label="Portrait of client" style="background:linear-gradient(135deg,#c9a27c,#4a3728)"></div><div class="who"><b>Tom<br>Barker</b><small>JOURNALIST</small></div><div class="quote">"Vestibulum morbi blandit cursus risus at ultrices. Tristique sollicitudin nibh sit amet! Siverra lectus mauris ultrices eros in"</div></div>
<div class="abs testi" style="left:466px;top:3391px"><div class="photo" role="img" aria-label="Portrait of client" style="background:linear-gradient(135deg,#b07a55,#3a2418)"></div><div class="who"><b>Anna<br>Vance</b><small>CUSTOMER</small></div><div class="quote">"Vestibulum morbi blandit cursus risus at ultrices. Tristique sollicitudin nibh sit amet! Siverra lectus mauris ultrices eros in"</div></div>
<div class="abs testi" style="left:762px;top:3391px"><div class="photo" role="img" aria-label="Portrait of client" style="background:linear-gradient(135deg,#d7b8a0,#8a3a2a)"></div><div class="who" style="top:70px"><b>Ella Moss</b><small>JOURNALIST</small></div><div class="quote">"Vestibulum morbi blandit cursus risus at ultrices. Tristique sollicitudin nibh sit amet! Siverra lectus mauris ultrices eros in"</div></div>
<div class="abs dots" style="left:578px;top:3718px;gap:6px"><i class="on" style="width:5px;height:5px;background:#333"></i><i style="width:5px;height:5px"></i><i style="width:5px;height:5px"></i><i style="width:5px;height:5px"></i></div>

<!-- blogs -->
<div class="abs h2" style="left:0;top:3914px;width:1200px">Blogs</div>
<div class="abs sub" style="top:3966px">Lorem ipsum dolor sit amet, consectetur adipiscing elit.<br>Mauris eros dolor pellentesque sed luctus dapibus lobortis orci.</div>

<div class="abs blog" style="left:66px;top:4104px"><div class="img" role="img" aria-label="Photo: mother and daughter talking" style="background:linear-gradient(135deg,#e8e2da,#6d7a84)"></div><h4>How To Be A Friend Of Your Daughter?</h4><p>Lorem ipsum dolor sit amet, consectetur adipiscing elit. Morbi volutpat justo sed efficitur cursus. Mauris fringilla quam vitae lacinia.</p><a>READ MORE</a></div>
<div class="abs blog" style="left:341px;top:4104px"><div class="img" role="img" aria-label="Photo: team leader in an office" style="background:linear-gradient(135deg,#6a6a6a,#1a1c1e)"></div><h4>How To Lead Your Team?</h4><p>Lorem ipsum dolor sit amet, consectetur adipiscing elit. Morbi volutpat justo sed efficitur cursus. Mauris fringilla quam vitae lacinia.</p><a>READ MORE</a></div>
<div class="abs blog" style="left:617px;top:4104px"><div class="img" role="img" aria-label="Photo: professional woman in a corridor" style="background:linear-gradient(135deg,#c8d4dc,#4f5c66)"></div><h4>Successful Career</h4><p>Lorem ipsum dolor sit amet, consectetur adipiscing elit. Morbi volutpat justo sed efficitur cursus. Mauris fringilla quam vitae lacinia.</p><a>READ MORE</a></div>
<div class="abs blog" style="left:892px;top:4104px"><div class="img" role="img" aria-label="Photo: man working at a laptop" style="background:linear-gradient(135deg,#dfe6ea,#5d6f7b)"></div><h4>The Self-Confidence That Leads You In Every Thing.</h4><p>Lorem ipsum dolor sit amet, consectetur adipiscing elit. Morbi volutpat justo sed efficitur cursus. Mauris fringilla quam vitae lacinia.</p><a>READ MORE</a></div>

<!-- footer -->
<svg class="abs" style="left:0;top:4690px" width="1200" height="130" viewBox="0 0 1200 130">
  <path d="M0 110 C250 20 520 0 760 40 C950 72 1080 80 1200 50 L1200 130 L0 130Z" fill="#1bb3a1"/>
  <path d="M0 125 C260 50 520 30 760 65 C960 95 1080 100 1200 80 L1200 130 L0 130Z" fill="#7fd8cc"/>
  <path d="M0 130 C270 80 520 62 770 90 C960 112 1080 118 1200 108 L1200 130Z" fill="#eef8f6"/>
</svg>
<div class="abs footer-bg"></div>
<div class="abs foot-logo">Rising Paths</div>
<p class="abs foot-about">Lorem ipsum dolor sit amet, consectetur adipiscing elit, sed do eiusmod tempor incididunt ut labore et dolore magna aliqua. Vulputate dignissim suspendisse in est ante. Faucibus turpis in eu mi bibendum neque. Sodales ut etiam sit amet nisl purus. Velit laoreet id donec ultrices tincidunt.</p>

<div class="abs foot-h" style="left:444px">Links</div>
<ul class="abs foot-links"><li>Home</li><li>About Me</li><li>My Services</li><li>Testimonies</li><li>Blogs</li><li>Contact</li></ul>

<div class="abs foot-h" style="left:617px">Contact</div>
<div class="abs foot-contact" style="top:4910px"><svg width="12" height="16" viewBox="0 0 12 16"><path d="M6 0a6 6 0 0 0-6 6c0 4.5 6 10 6 10s6-5.5 6-10a6 6 0 0 0-6-6zm0 8.5A2.5 2.5 0 1 1 6 3.5a2.5 2.5 0 0 1 0 5z" fill="#1bb3a1"/></svg><span>12/7 Maple Row<br>Eastfield</span></div>
<div class="abs foot-contact" style="top:4980px"><svg width="15" height="15" viewBox="0 0 24 24"><path d="M6.6 10.8a15 15 0 0 0 6.6 6.6l2.2-2.2a1 1 0 0 1 1-.25 11.4 11.4 0 0 0 3.6.57 1 1 0 0 1 1 1V20a1 1 0 0 1-1 1A17 17 0 0 1 3 4a1 1 0 0 1 1-1h3.5a1 1 0 0 1 1 1c0 1.25.2 2.45.57 3.57a1 1 0 0 1-.25 1z" fill="#1bb3a1"/></svg><span>+0198765432</span></div>
<div class="abs foot-contact" style="top:5020px"><svg width="16" height="12" viewBox="0 0 16 12"><rect width="16" height="12" rx="1" fill="#1bb3a1"/><path d="M0 1l8 6 8-6" stroke="#eef8f6" stroke-width="1.5" fill="none"/></svg><span>hello@mailbox.com</span></div>
<div class="abs socials" style="left:608px;top:5098px;color:var(--teal)"><i></i><i></i><i></i><i></i></div>

<div class="abs foot-h" style="left:845px">Book An Appointment</div>
<div class="abs form-label" style="left:836px;top:4916px">Name</div>
<div class="abs form-label" style="left:947px;top:4916px">Email</div>
<div class="abs field" style="left:836px;top:4934px;width:103px">Name</div>
<div class="abs field" style="left:947px;top:4934px;width:103px">Email</div>
<div class="abs form-label" style="left:836px;top:4984px">Select Service</div>
<div class="abs field" style="left:836px;top:5000px;width:214px;height:33px;padding-top:9px;color:#444">Growth Career<span style="position:absolute;right:8px;top:7px">⌄</span></div>
<div class="abs form-label" style="left:836px;top:5048px">Date</div>
<div class="abs form-label" style="left:947px;top:5048px">Time</div>
<div class="abs field" style="left:836px;top:5066px;width:103px">Date</div>
<div class="abs field" style="left:947px;top:5066px;width:103px">Time</div>
<div class="abs schedule">Schedule Now »</div>

<div class="abs copy">Copyright © 2022 RisingPaths</div>
</body>
</html>
```